Thorne Consulting, Business Cards for International Development Consultancy

I'm an independent consultant working in the international development sector. I work with small organisations in developing countries to help them develop their community based programs so that they can be internationally competitive. This means they need to work better with their own communities to deliver meaningful quality work and also improve the accountability of their work so that they can compete for international and domestic funding.

I like the idea of being a connector between community, local organisations and international best practice and back again (ie acknowledging that international best practice can learn a lot from community).

My surname is Thorne - so I'd like the logo to use the idea of web as a connector.

I work with people with sight impairments - would like my card to be useful for low vision (i.e. clear graphics, easy to read font) and no vision (i.e. brail).

Target Market(s)

international non-government organisations (i.e. harvestaid, bright futures trust, open horizons), Blue Anchor Relief Alliance, government (i.e. Australian Bureau of Overseas Partnerships, consulars), non government agencies,

Industry/Entity Type

Business

Contact Information for Business Card

International Development Consultant
Linking Global Development Practice with Local People

Kerry Thorne
Lead Consultant
Phone: +61 417 382519
Email: kthorne.consulting@mailvale.com

Font styles to use
Sans Serif

Colors
eaf1f7
85acd3
d3a5cc
0456a4
a64599
0255a3

Requirements
Nice to have
• brail
Should not have
• fancy fonts - needs to be easy to read.

```html
<!DOCTYPE html>
<html lang="en">
<head>
<meta charset="utf-8">
<title>Thorne Consulting – Business Cards</title>
<link rel="stylesheet" href="https://fonts.googleapis.com/css2?family=Questrial&family=Michroma&display=swap">
<style>
  :root {
    --page-bg: #e9e6e2;
    --card-white: #ffffff;
    --card-white-shade: #eef0f2;
    --ink-dark: #2a2a2a;
    --ink-grey: #444b52;
    --brand-blue: #0456a4;
    --brand-blue-mid: #1464c8;
    --brand-blue-light: #85acd3;
    --silver: #e4e8ee;
  }
  * { box-sizing: border-box; margin: 0; padding: 0; }
  html, body { width: 1200px; height: 800px; overflow: hidden; }
  body {
    background: var(--page-bg);
    font-family: "Questrial", "Century Gothic", sans-serif;
    position: relative;
  }
  .card {
    position: absolute;
    top: 250px;
    width: 520px;
    height: 300px;
    border-radius: 4px;
    box-shadow: 0 10px 28px rgba(0,0,0,0.18);
    overflow: hidden;
  }
  .card--front {
    left: 50px;
    background: linear-gradient(135deg, var(--card-white-shade) 0%, var(--card-white) 45%, var(--card-white-shade) 100%);
  }
  .card--back {
    left: 630px;
    background: linear-gradient(160deg, var(--brand-blue-mid) 0%, var(--brand-blue) 100%);
  }
  .contact-line {
    position: absolute;
    display: flex;
    align-items: center;
    gap: 8px;
    color: var(--ink-dark);
    font-size: 15px;
    font-weight: 700;
    white-space: nowrap;
  }
  .contact-line svg { width: 16px; height: 16px; fill: var(--brand-blue); flex: none; }
  .contact-line--phone { left: 34px; top: 96px; }
  .contact-line--email { left: 200px; top: 168px; }
  .identity { position: absolute; left: 212px; top: 80px; }
  .identity__name {
    font-size: 26px;
    font-weight: 700;
    color: var(--ink-grey);
    letter-spacing: 0.3px;
    line-height: 1.1;
  }
  .identity__role {
    font-size: 15px;
    font-style: italic;
    color: var(--brand-blue-mid);
    margin-top: 3px;
  }
  .tagline {
    position: absolute;
    left: 34px;
    bottom: 30px;
    font-size: 16px;
    color: var(--brand-blue-mid);
    white-space: nowrap;
  }
  .brand {
    position: absolute;
    inset: 0;
    display: flex;
    align-items: center;
    justify-content: center;
    gap: 16px;
  }
  .brand__mark {
    width: 28px;
    height: 28px;
    border: 2px solid var(--silver);
    border-radius: 50%;
    flex: none;
  }
  .brand__name {
    font-family: "Michroma", "Eurostile", sans-serif;
    font-size: 22px;
    letter-spacing: 5px;
    color: var(--silver);
    white-space: nowrap;
  }
</style>
</head>
<body>
  <section class="card card--front" aria-label="Business card front">
    <div class="contact-line contact-line--phone">
      <svg viewBox="0 0 24 24" aria-hidden="true"><path d="M6.6 10.8a15.1 15.1 0 0 0 6.6 6.6l2.2-2.2a1 1 0 0 1 1-.25 11.4 11.4 0 0 0 3.6.57 1 1 0 0 1 1 1V20a1 1 0 0 1-1 1A17 17 0 0 1 3 4a1 1 0 0 1 1-1h3.5a1 1 0 0 1 1 1c0 1.25.2 2.45.57 3.57a1 1 0 0 1-.25 1z"/></svg>
      <span>+61 417 382519</span>
    </div>
    <div class="identity">
      <h1 class="identity__name">Kerry Thorne</h1>
      <p class="identity__role">Lead Consultant</p>
    </div>
    <div class="contact-line contact-line--email">
      <svg viewBox="0 0 24 24" aria-hidden="true"><path d="M2 5h20v14H2V5zm2 2v.3l8 5.2 8-5.2V7H4zm16 2.7-8 5.2-8-5.2V17h16V9.7z"/></svg>
      <span>kthorne.consulting@mailvale.com</span>
    </div>
    <p class="tagline">Linking Global Development Practice with Local People</p>
  </section>

  <section class="card card--back" aria-label="Business card back">
    <div class="brand">
      <span class="brand__mark" aria-hidden="true"></span>
      <p class="brand__name">THORNE CONSULTING</p>
    </div>
  </section>
</body>
</html>
```